Football tournament flyer

I would like a quick turn around for this please.
I need a flyer to promote an 11 aside football tournament I am organising to celebrate the 23rd independence of my country Somaliland. Please use the national colours of our flag in the flyer, I have attached a file for your consideration.
The tournament will take place on 10/05/2014, from 9am - 8pm. The venue will be Corrin Open Space, Tavistrel Lane, Enfield, EN7 2QR.
Refreshments, food and entertainment will be provided.
The name of the cup is Warsadle Cup.
Spaces are limited and the entry fee per team is £200. All proceeds are for charity projects in Somaliland.
To register a team contact Faisal Warsame on 07521 804 192 or Bashir Yusuf on 07463 125 870.
The best players will have the opportunity to represent Somaliland in an international game on the 17/05/2014.
The tournament is organised by Dalmar FC and EverKindred Foundation.

```html
<!DOCTYPE html>
<html lang="en">
<head>
<meta charset="utf-8">
<title>Warsadle Cup – 11 Aside Football Tournament</title>
<link rel="stylesheet" href="https://fonts.googleapis.com/css2?family=Arimo:wght@700&family=Cinzel:wght@700&family=Kaushan+Script&family=Tinos:wght@400;700&display=swap">
<style>
  :root {
    --frame: #1c1512;
    --curtain-deep: #7a0d12;
    --curtain: #b3161c;
    --glow: #e8561f;
    --amber: #f39a2a;
    --stadium: #143f8f;
    --stadium-deep: #0b2350;
    --pitch: #2f9a3a;
    --pitch-light: #63c14e;
    --white: #ffffff;
    --yellow: #ffe100;
    --red: #e3221b;
    --ribbon: #d9d9d9;
    --ink: #1a1a1a;
  }
  * { margin: 0; padding: 0; box-sizing: border-box; }
  html, body { width: 935px; height: 1200px; overflow: hidden; background: var(--frame); }
  .flyer { position: relative; width: 935px; height: 1200px; background: var(--frame); }
  .flyer-body {
    position: absolute; left: 27px; top: 27px; width: 881px; height: 1146px; overflow: hidden;
  }
  .scene-backdrop {
    position: absolute; inset: 0;
    background: linear-gradient(180deg, var(--curtain-deep) 0%, var(--curtain) 22%, var(--glow) 48%, var(--amber) 64%, var(--stadium) 70%, var(--stadium-deep) 82%, var(--pitch) 86%, var(--pitch-light) 93%, var(--stadium-deep) 100%);
  }
  .football {
    position: absolute; left: 384px; top: 0; width: 108px; height: 96px;
    border-radius: 50%; background: radial-gradient(circle at 40% 35%, #ffffff 0%, #d6d6d6 60%, #5a5a5a 100%);
  }
  .thumb-art {
    position: absolute; left: 88px; top: 339px; width: 150px; height: 257px; border-radius: 40px;
    background: radial-gradient(ellipse at 50% 50%, rgba(255,255,255,.9) 0%, #f0d0c0 45%, rgba(227,34,27,.0) 75%);
  }
  .ribbon {
    position: absolute; left: 123px; top: 73px; width: 635px; height: 76px;
  }
  .ribbon-text {
    position: absolute; left: 123px; top: 80px; width: 635px; text-align: center;
    font-family: "Kaushan Script", cursive; font-size: 30px; color: var(--ink);
  }
  .ribbon-text .num { font-size: 38px; }
  .organisers { position: absolute; left: 0; width: 100%; text-align: center; font-family: "Arimo", sans-serif; color: var(--yellow); }
  .organisers-label { top: 180px; font-size: 30px; }
  .organisers-names { top: 218px; font-size: 20px; }
  .cup-name {
    position: absolute; left: 0; width: 100%; text-align: center;
    font-family: "Cinzel", serif; color: var(--white); -webkit-text-stroke: 2px var(--red);
    text-shadow: 3px 4px 0 rgba(90,0,0,.5);
  }
  .cup-title { top: 242px; font-size: 100px; letter-spacing: 1px; }
  .cup-word { top: 352px; font-size: 54px; }
  .event-lines { position: absolute; left: 0; width: 100%; text-align: center; font-family: "Tinos", serif; font-weight: 700; color: var(--white); }
  .format { top: 420px; font-size: 56px; -webkit-text-stroke: 1px var(--ink); left: 20px; }
  .sport { top: 500px; font-size: 38px; line-height: 44px; left: 20px; }
  .date { top: 588px; font-size: 38px; left: 20px; }
  .venue {
    position: absolute; left: 20px; width: 100%; top: 646px; text-align: center;
    font-family: "Tinos", serif; font-size: 21px; line-height: 25px; color: var(--white);
  }
  .entry-note {
    position: absolute; left: 585px; top: 378px; width: 260px; text-align: center;
    font-family: "Tinos", serif; font-size: 22px; line-height: 26px; color: var(--white);
    transform: rotate(-4deg);
  }
  .entry-note em { font-weight: 700; }
  .entry-note .fee { color: var(--yellow); font-weight: 700; font-size: 30px; font-style: italic; }
  .welcome-ribbon { position: absolute; left: 325px; top: 780px; width: 245px; height: 42px; }
  .welcome-text {
    position: absolute; left: 325px; top: 788px; width: 245px; text-align: center;
    font-family: "Tinos", serif; font-weight: 700; font-size: 19px; color: var(--ink);
  }
  .selection-note {
    position: absolute; left: 30px; top: 860px; width: 820px; text-align: center;
    font-family: "Arimo", sans-serif; font-size: 26px; line-height: 34px; color: var(--white);
    transform: rotate(-5deg);
  }
  .contact-heading {
    position: absolute; left: 0; width: 100%; top: 1035px; text-align: center;
    font-family: "Arimo", sans-serif; font-size: 40px; color: var(--red);
    -webkit-text-stroke: 1px var(--white);
  }
  .contact-details {
    position: absolute; left: 0; width: 100%; top: 1092px; text-align: center;
    font-family: "Arimo", sans-serif; font-size: 22px; color: var(--white);
    word-spacing: 1px;
  }
  .contact-details .or { margin: 0 18px; }
</style>
</head>
<body>
<main class="flyer">
  <div class="flyer-body">
    <div class="scene-backdrop" role="img" aria-label="Red stage curtain glowing orange, opening onto a floodlit football stadium with crowd and green pitch"></div>
    <div class="football" role="img" aria-label="Football"></div>

    <svg class="ribbon" viewBox="0 0 635 76" aria-hidden="true">
      <polygon points="0,20 70,20 70,70 0,70 20,45" fill="#bdbdbd"/>
      <polygon points="635,20 565,20 565,70 635,70 615,45" fill="#bdbdbd"/>
      <path d="M45,8 Q317,-4 590,8 L590,62 Q317,50 45,62 Z" fill="var(--ribbon)" stroke="#9a9a9a" stroke-width="1"/>
    </svg>
    <p class="ribbon-text">Celebrating <span class="num">23rd</span> Independence day</p>

    <p class="organisers organisers-label">Organised by</p>
    <p class="organisers organisers-names">Dalmar FC and&nbsp; EverKindred Foundation</p>

    <h1 class="cup-name cup-title">WARSADLE</h1>
    <p class="cup-name cup-word">CUP</p>

    <div class="thumb-art" role="img" aria-label="Thumbs-up hand painted in the green, white and red of the Somaliland flag with a black star"></div>

    <p class="event-lines format">11 ASIDE</p>
    <p class="event-lines sport">FOOTBALL<br>TOURNAMENT</p>
    <p class="event-lines date">10/05/2014 from 9am - 8pm</p>
    <p class="venue">Corrin Open Space, Tavistrel Lane,<br>Enfield, EN7 2QR.<br>Refreshments, food and<br>entertainment will be provided.</p>

    <p class="entry-note">Spaces are limited and the <em>entry fee per team is</em><br><span class="fee">£200.</span><br>All proceeds are for charity projects in Somaliland.</p>

    <svg class="welcome-ribbon" viewBox="0 0 245 42" aria-hidden="true">
      <polygon points="0,10 40,10 40,38 0,38 14,24" fill="#bdbdbd"/>
      <polygon points="245,10 205,10 205,38 245,38 231,24" fill="#bdbdbd"/>
      <rect x="25" y="4" width="195" height="30" fill="var(--ribbon)"/>
    </svg>
    <p class="welcome-text">Welcome</p>

    <p class="selection-note">*The best players will have the opportunity to represent Somaliland<br>in an international game on the 17/05/2014.</p>

    <h2 class="contact-heading">To Register A Team Contact</h2>
    <p class="contact-details">Faisal Warsame on 07521 804 192<span class="or">or</span>Bashir Yusuf on 07463 125 870.</p>
  </div>
</main>
</body>
</html>
```